High End Clothing Line Needs Stationary Design

We need a stationery design including letterhead and envelopes for a new Christian clothing company called Covenant 9 based out of New York. Our company colors are charcoal gray and silver. The final design needs to be modern, simple, and have a high end look to it.

Industry/Entity Type

Clothing

Font styles to use
Sans Serif

Colors
474747
cfcfcf

Requirements
Must have
• On the top of page in center we would like a dark gray solid box with logo inside in light gray. Name, email, title, phone # must be on bottom of the page.
• Light gray cross will be on black flap of envelope. Entire back flap in dark gray. Eventually logo and cross will be done in silver stamping when project complete.
Nice to have
• Would like to see how just the logo without Covenant 9 looks in middle of letterhead faded in background.

```html
<!DOCTYPE html>
<html lang="en">
<head>
<meta charset="utf-8">
<title>Covenant 9 Stationery</title>
<link href="https://fonts.googleapis.com/css2?family=Questrial&display=swap" rel="stylesheet">
<style>
  :root{
    --charcoal:#1f1f1d;
    --charcoal-soft:#2a2a28;
    --silver:#cfcfcf;
    --paper:#f1f1f1;
    --ink:#474747;
    --backdrop:#d3d3d3;
    --rule:#8a8a8a;
  }
  *{margin:0;padding:0;box-sizing:border-box}
  html,body{width:1200px;height:1000px;overflow:hidden}
  body{background:var(--backdrop);font-family:"Questrial",sans-serif;color:var(--ink);position:relative}
  .piece{position:absolute;overflow:hidden}
  .brand-name{font-family:"Questrial",sans-serif;font-weight:400;color:var(--silver);white-space:nowrap;text-align:center}

  .folder{left:152px;top:42px;width:458px;height:558px;background:var(--charcoal);border-radius:4px}
  .folder .spine{position:absolute;left:20px;top:0;width:2px;height:100%;background:#151514}
  .folder .brand-name{position:absolute;left:0;right:0;top:150px;font-size:28px;letter-spacing:2px}
  .folder .faint-name{position:absolute;left:40px;top:330px;font-size:120px;color:var(--charcoal-soft);white-space:nowrap;line-height:1}

  .letterhead{left:616px;top:60px;width:417px;height:540px;background:var(--paper)}
  .logo-box{position:absolute;background:var(--charcoal);display:flex;align-items:center;justify-content:center}
  .letterhead .logo-box{left:152px;top:0;width:112px;height:90px}
  .logo-box .brand-name{font-size:16px;letter-spacing:1px}
  .letterhead .faint-name{position:absolute;left:0;right:0;top:250px;text-align:center;font-size:78px;color:#e4e4e4;line-height:1}
  .footer-rule{position:absolute;height:3px;border-top:1px solid var(--rule);border-bottom:1px solid var(--rule)}
  .letterhead .footer-rule{left:46px;right:46px;top:510px}
  .letterhead .contact{position:absolute;left:0;right:0;top:517px;text-align:center;font-size:6px;letter-spacing:.3px}
  .letterhead .contact span{margin:0 5px}

  .envelope-front{left:117px;top:630px;width:466px;height:200px;background:var(--paper)}
  .envelope-front .logo-box{left:25px;top:0;width:112px;height:88px}
  .envelope-front .footer-rule{left:18px;width:127px;top:174px}
  .envelope-front .address{position:absolute;left:18px;top:184px;font-size:6px}

  .envelope-back{left:617px;top:630px;width:466px;height:200px;background:var(--paper)}
  .envelope-back svg{position:absolute;left:0;top:0}

  .card{top:860px;width:178px;height:98px}
  .card-contact{left:410px;background:var(--paper)}
  .card-contact .dark-half{position:absolute;left:0;top:0;width:84px;height:100%;background:var(--charcoal)}
  .card-contact svg{position:absolute;left:30px;top:25px}
  .card-contact .details{position:absolute;left:98px;top:27px;font-size:5px;line-height:7px}
  .card-contact .name{font-size:6px;font-weight:700;color:#222}
  .card-contact .role{margin-bottom:7px}
  .card-brand{left:616px;width:172px;background:var(--charcoal);display:flex;align-items:center;justify-content:center}
  .card-brand .brand-name{font-size:17px;letter-spacing:1px}
</style>
</head>
<body>
  <section class="piece folder" aria-label="Presentation folder">
    <div class="spine"></div>
    <p class="faint-name" aria-hidden="true">Covenant 9</p>
    <p class="brand-name">Covenant 9</p>
  </section>

  <section class="piece letterhead" aria-label="Letterhead">
    <p class="faint-name" aria-hidden="true">Covenant 9</p>
    <div class="logo-box"><p class="brand-name">Covenant 9</p></div>
    <div class="footer-rule"></div>
    <p class="contact"><span>DANIEL MORENO</span><span>CEO/Founder</span><span>5550102468</span><span>danielmoreno9@mail.com</span></p>
  </section>

  <section class="piece envelope-front" aria-label="Envelope front">
    <div class="logo-box"><p class="brand-name">Covenant 9</p></div>
    <div class="footer-rule"></div>
    <p class="address">14 Harbor Ln, Eastport Station, NY 11941</p>
  </section>

  <section class="piece envelope-back" aria-label="Envelope back">
    <svg width="466" height="200" viewBox="0 0 466 200">
      <polygon points="0,0 466,0 466,8 440,65 26,65 0,8" fill="#1f1f1d"/>
      <polygon points="233,12 235,30 252,33 235,35 233,54 231,35 214,33 231,30" fill="#cfcfcf"/>
    </svg>
  </section>

  <section class="piece card card-contact" aria-label="Business card front">
    <div class="dark-half"></div>
    <svg width="24" height="46" viewBox="0 0 24 46">
      <polygon points="12,0 13.3,17 24,19 13.3,21 12,46 10.7,21 0,19 10.7,17" fill="#cfcfcf"/>
    </svg>
    <div class="details">
      <p class="name">DANIEL MORENO</p>
      <p class="role">CEO/Founder</p>
      <p><b>T:</b> 555.010.2468</p>
      <p><b>E:</b> danielmoreno9@mail.com</p>
      <p><b>W:</b> covenant9clothing.com</p>
    </div>
  </section>

  <section class="piece card card-brand" aria-label="Business card back">
    <p class="brand-name">Covenant 9</p>
  </section>
</body>
</html>
```